Design some Stationery and Business Cards

I need help with stationary (letters and envelopes) layout and business card layouts. I would like something modern/clean with the typeface and some clean layouts. I've attached a few samples along the lines of what I was thinking, but please use your best judgement. Also, I've attached the logo - can you remove the "LLC" part in the final rendering? Also, please be patient with any back and forth to tweak the design layout.

As for the contact info here is information

Dorian P. Welbeck, Esq.

418 Cobalt Lane, Suite 7
Reading, MA 02493

P: 781-555-3172
C: 857-555-6031
E: Dorian@[login to view URL]

```html
<!DOCTYPE html>
<html lang="en">
<head>
<meta charset="UTF-8">
<title>Welbeck Law LLC — Business Card</title>
<link href="https://fonts.googleapis.com/css2?family=Lato:wght@300;400;700&display=swap" rel="stylesheet">
<style>
  :root {
    --backdrop: #a4a4a4;
    --card: #ffffff;
    --pattern-tint: #f3f3f5;
    --navy: #2c2669;
    --ink: #2a2a2a;
    --muted: #6a6a72;
    --rule: #2a2a2a;
  }
  * { margin: 0; padding: 0; box-sizing: border-box; }
  html, body {
    width: 1200px;
    height: 900px;
    overflow: hidden;
    background: var(--backdrop);
    font-family: "Lato", sans-serif;
  }
  .stage { position: relative; width: 1200px; height: 900px; }

  .card {
    position: absolute;
    width: 640px;
    height: 366px;
    background: var(--card);
    box-shadow: 0 10px 24px rgba(0,0,0,0.25);
  }

  /* Front side */
  .card-front { left: 110px; top: 80px; }
  .card-front .pattern-field {
    position: absolute; inset: 0;
    background: var(--pattern-tint);
  }
  .card-front .firm-name {
    position: absolute;
    left: 0; right: 0; top: 158px;
    text-align: center;
    color: var(--navy);
    font-weight: 400;
    font-size: 34px;
    letter-spacing: 3px;
  }

  /* Back side */
  .card-back { left: 450px; top: 450px; }
  .card-back .firm-name {
    position: absolute;
    left: 0; right: 0; top: 52px;
    text-align: center;
    color: var(--navy);
    font-weight: 400;
    font-size: 20px;
    letter-spacing: 2px;
  }
  .identity {
    position: absolute;
    left: 0; right: 0; top: 104px;
    text-align: center;
  }
  .identity .person {
    color: var(--navy);
    font-size: 24px;
    font-weight: 400;
  }
  .identity .person strong { font-weight: 700; }
  .identity .role {
    color: var(--muted);
    font-size: 16px;
    font-weight: 400;
    margin-top: 2px;
  }
  .divider {
    position: absolute;
    left: 319px; top: 212px;
    width: 2px; height: 74px;
    background: var(--rule);
  }
  .contact-list {
    position: absolute;
    left: 36px; top: 236px;
    list-style: none;
  }
  .contact-list li {
    display: flex;
    align-items: center;
    gap: 14px;
    color: var(--ink);
    font-size: 17px;
    line-height: 34px;
  }
  .contact-list svg { width: 14px; height: 14px; fill: var(--ink); flex: none; }
  .address {
    position: absolute;
    left: 360px; top: 196px;
    color: var(--ink);
    font-size: 17px;
    line-height: 26px;
    font-style: normal;
  }
</style>
</head>
<body>
<div class="stage">

  <section class="card card-front">
    <div class="pattern-field" role="img" aria-label="Faint repeating monogram pattern across the card face"></div>
    <div class="firm-name">WELBECK LAW LLC</div>
  </section>

  <section class="card card-back">
    <div class="firm-name">WELBECK LAW LLC</div>

    <div class="identity">
      <div class="person"><strong>Dorian P.</strong> Welbeck, Esq.</div>
      <div class="role">Attorney At Law</div>
    </div>

    <ul class="contact-list">
      <li>
        <svg viewBox="0 0 14 14" aria-hidden="true"><path d="M1 4c0-2 12-2 12 0v1.5h-3.5V4h-5v1.5H1z M3 7h8l1.5 5h-11z"/></svg>
        781-555-3172
      </li>
      <li>
        <svg viewBox="0 0 14 14" aria-hidden="true"><path d="M3.5 0.5h7v13h-7z M4.7 1.7v10.6h4.6V1.7z" fill-rule="evenodd"/></svg>
        857-555-6031
      </li>
      <li>
        <svg viewBox="0 0 14 14" aria-hidden="true"><path d="M0.5 3h13v8h-13z M1.5 4l5.5 4 5.5-4z" fill-rule="evenodd"/></svg>
        dorian@wblaw.com
      </li>
    </ul>

    <div class="divider"></div>

    <address class="address">
      418 Cobalt Lane, Suite 7<br>
      Reading, MA 02493
    </address>
  </section>

</div>
</body>
</html>
```